Small Business Consulting Firm Needs Business Card Design

Need a sleek modern business card with 2 sides matching the colors of our logo. We will be placing these with a mailer we are sending out. These business cards will only ever be given to business owners. We operate helping businesses who are struggling with cash flow or finances. If the green and blue design needs to be moved to the right of "Harborline Crest Consulting" for aesthetic purposes that is ok. We will need an editable file if possible. We would like to include the reps name, email, website, and phone number. For now just use Peter Vance, pvance@harborlinecrest.com, www.harborlinecrest.com, and 833-555-0172.

```html
<!DOCTYPE html>
<html lang="en">
<head>
<meta charset="utf-8">
<title>Harborline Crest Consulting — Business Card</title>
<link href="https://fonts.googleapis.com/css2?family=Montserrat:wght@400&family=Open+Sans:wght@400;700&display=swap" rel="stylesheet">
<style>
  :root {
    --green: #7dbb4d;
    --green-dark: #5f9a38;
    --green-mid: #6fae42;
    --blue: #0a7bc1;
    --blue-dark: #24608f;
    --ink: #3a3a3a;
    --white: #ffffff;
    --backdrop: #d3d3d3;
  }
  * { margin: 0; padding: 0; box-sizing: border-box; }
  html, body { width: 1200px; height: 803px; overflow: hidden; }
  body {
    background: var(--backdrop);
    font-family: "Open Sans", Arial, sans-serif;
    position: relative;
  }
  .card {
    position: absolute;
    top: 247px;
    width: 540px;
    height: 309px;
    overflow: hidden;
    box-shadow: 0 3px 10px rgba(0,0,0,0.18);
  }
  .card--front { left: 40px; background: var(--white); }
  .card--back { left: 620px; background: var(--green); }

  .card__bands { position: absolute; inset: 0; width: 100%; height: 100%; }

  .brand {
    position: absolute;
    display: flex;
    align-items: center;
    gap: 10px;
  }
  .brand__mark { width: 22px; height: 22px; flex: none; }
  .brand__name {
    font-family: "Montserrat", Arial, sans-serif;
    font-weight: 400;
    font-size: 17px;
    letter-spacing: 2px;
    text-transform: uppercase;
    white-space: nowrap;
  }
  .card--front .brand { left: 36px; top: 178px; }
  .card--front .brand__mark { background: var(--green); }
  .card--front .brand__name { color: var(--ink); }

  .card--back .brand { left: 50%; top: 50%; transform: translate(-50%, -50%); }
  .card--back .brand__mark { background: var(--white); }
  .card--back .brand__name { color: var(--white); font-size: 19px; }

  .contact {
    position: absolute;
    left: 300px;
    top: 44px;
    color: var(--ink);
  }
  .contact__name {
    font-weight: 700;
    font-size: 16px;
    color: var(--green);
    text-transform: uppercase;
    margin-bottom: 6px;
  }
  .contact__line {
    display: flex;
    align-items: center;
    gap: 7px;
    font-size: 11.5px;
    line-height: 19px;
  }
  .contact__icon { width: 11px; height: 11px; flex: none; fill: var(--blue); }
</style>
</head>
<body>
  <section class="card card--front" aria-label="Business card front">
    <svg class="card__bands" viewBox="0 0 540 309" preserveAspectRatio="none" aria-hidden="true">
      <polygon points="250,309 540,309 540,180" fill="var(--blue)"/>
      <polygon points="285,309 540,309 540,200" fill="var(--blue-dark)"/>
      <polygon points="395,262 540,40 540,180" fill="var(--green-mid)"/>
      <polygon points="420,250 540,60 540,80" fill="var(--green-dark)"/>
      <polygon points="430,245 540,120 540,180" fill="var(--green)"/>
    </svg>

    <div class="brand">
      <span class="brand__mark"></span>
      <span class="brand__name">Harborline Crest Consulting</span>
    </div>

    <div class="contact">
      <p class="contact__name">Peter Vance</p>
      <p class="contact__line">
        <svg class="contact__icon" viewBox="0 0 24 24" aria-hidden="true"><path d="M6.6 10.8a15.1 15.1 0 0 0 6.6 6.6l2.2-2.2a1 1 0 0 1 1-.25 11.4 11.4 0 0 0 3.6.57 1 1 0 0 1 1 1V20a1 1 0 0 1-1 1A17 17 0 0 1 3 4a1 1 0 0 1 1-1h3.5a1 1 0 0 1 1 1c0 1.25.2 2.45.57 3.57a1 1 0 0 1-.25 1z"/></svg>
        833-555-0172
      </p>
      <p class="contact__line">
        <svg class="contact__icon" viewBox="0 0 24 24" aria-hidden="true"><path d="M2 5h20v14H2z M2 5l10 8 10-8" fill="none" stroke="var(--blue)" stroke-width="2.4"/></svg>
        pvance@harborlinecrest.com
      </p>
      <p class="contact__line">
        <svg class="contact__icon" viewBox="0 0 24 24" aria-hidden="true"><g fill="none" stroke="var(--blue)" stroke-width="2.2"><circle cx="12" cy="12" r="10"/><path d="M2 12h20M12 2c3 3 3 17 0 20M12 2c-3 3-3 17 0 20"/></g></svg>
        www.harborlinecrest.com
      </p>
    </div>
  </section>

  <section class="card card--back" aria-label="Business card back">
    <div class="brand">
      <span class="brand__mark"></span>
      <span class="brand__name">Harborline Crest Consulting</span>
    </div>
  </section>
</body>
</html>
```